Stone Arch Letterhead

I just need letterhead for my integrative psychiatry business. I'm going to use this to do mailings to other doctors, as well as send letters to patients. Thank you

```html
<!DOCTYPE html>
<html lang="en">
<head>
<meta charset="utf-8">
<title>Stone Arch Letterhead</title>
<link rel="stylesheet" href="https://fonts.googleapis.com/css2?family=Source+Sans+3:wght@400;600&display=swap">
<style>
  :root {
    --paper: #ffffff;
    --ink: #4a4a4a;
    --brand-green: #3f7a3b;
    --brand-brown: #5b3a22;
    --icon: #3c4a3a;
    --rule: #9a9a9a;
  }
  * { margin: 0; padding: 0; box-sizing: border-box; }
  html, body {
    width: 929px;
    height: 1200px;
    overflow: hidden;
    background: var(--paper);
  }
  .letterhead {
    position: relative;
    width: 929px;
    height: 1200px;
    background: var(--paper);
    font-family: "Source Sans 3", Arial, sans-serif;
    color: var(--ink);
  }
  .brand {
    position: absolute;
    left: 30px;
    top: 78px;
    display: flex;
    align-items: center;
    gap: 12px;
  }
  .brand-dot {
    width: 34px;
    height: 34px;
    border-radius: 50%;
    background: var(--brand-brown);
  }
  .brand-name {
    font-size: 38px;
    font-weight: 600;
    color: var(--brand-green);
    line-height: 1;
  }
  .contact {
    position: absolute;
    left: 664px;
    top: 56px;
    padding-left: 24px;
    border-left: 1.5px solid var(--rule);
    list-style: none;
  }
  .contact li {
    display: flex;
    align-items: center;
    gap: 8px;
    font-size: 14px;
    height: 27px;
  }
  .contact svg { width: 11px; height: 11px; fill: var(--icon); flex: none; }
  .address {
    position: absolute;
    left: 22px;
    top: 1138px;
    font-size: 15.5px;
    line-height: 23px;
    font-style: normal;
  }
</style>
</head>
<body>
<main class="letterhead">
  <header>
    <div class="brand">
      <span class="brand-dot"></span>
      <span class="brand-name">Stone Arch</span>
    </div>
    <ul class="contact">
      <li>
        <svg viewBox="0 0 12 12" aria-hidden="true"><circle cx="6" cy="6" r="6"/><path d="M4 3.2c.4-.3.8 0 1 .5l.3.8c.1.3 0 .5-.2.7l-.3.3c.3.8.9 1.4 1.7 1.7l.3-.3c.2-.2.4-.3.7-.2l.8.3c.5.2.8.6.5 1-.4.6-1 .9-1.7.7C5.2 8.2 3.8 6.8 3.3 4.9c-.2-.7.1-1.3.7-1.7z" fill="#fff"/></svg>
        <span>555-210-4836</span>
      </li>
      <li>
        <svg viewBox="0 0 12 12" aria-hidden="true"><rect x="3" y="1" width="6" height="3"/><rect x="0.5" y="4" width="11" height="5" rx="1"/><rect x="3" y="7.5" width="6" height="3.5" fill="#fff" stroke="#3c4a3a" stroke-width="1"/></svg>
        <span>555-210-4837</span>
      </li>
      <li>
        <svg viewBox="0 0 12 12" aria-hidden="true"><circle cx="6" cy="6" r="6"/><path d="M1 6h10M6 1c-2 2.8-2 7.2 0 10M6 1c2 2.8 2 7.2 0 10" stroke="#fff" stroke-width="0.9" fill="none"/></svg>
        <span>www.stonearchcare.example</span>
      </li>
    </ul>
  </header>
  <footer>
    <address class="address">
      2870 Meadowlark Lane, Suite 310<br>
      Fair Haven, CA 95812
    </address>
  </footer>
</main>
</body>
</html>
```